Simple Business Cards for Self-employed Coach

Simple business card with a design that includes the QLT logo.
Using either only the logo color or additional colors that match the logo.

Meridian Guides reach deeply into the past, gathering wisdom from East and West, while still staying current with the frontiers of new discovery in cognitive science, genetics, and other disciplines. see https://www.brightharborpath.example/what-is-integral-coaching/

Target Market(s)

Coaching Clients in Tokyo /Asia; in business organizations, but also outside

Industry/Entity Type

Life Coaching

Contact Information for Business Card

Lukas Brenning
Certified Meridian Guide

3-2-48 Kamiyoshi
Nakarino 164-0392
Tokyo, Japan

Phone: +81 70 4817 5062
E-Mail: lukas.brenning@mailora.example

Font styles to use
Sans Serif

Colors
00a990

Requirements
Must have
• include uploaded logo
• color fitting with QLT logo color
Nice to have
• simple, elegant design
Should not have
• clutter

```html
<!DOCTYPE html>
<html lang="en">
<head>
<meta charset="utf-8">
<title>Lukas Brenning — Business Card</title>
<link href="https://fonts.googleapis.com/css2?family=Libre+Franklin:wght@400;500;600&display=swap" rel="stylesheet">
<style>
  :root {
    --teal: #007a6c;
    --ink: #333333;
    --paper: #ffffff;
    --edge: #222222;
  }
  html, body {
    margin: 0;
    padding: 0;
    width: 960px;
    height: 1200px;
    overflow: hidden;
    background: var(--paper);
  }
  .canvas {
    position: relative;
    width: 960px;
    height: 1200px;
    font-family: "Libre Franklin", Arial, sans-serif;
  }
  .card {
    position: absolute;
    left: 180px;
    top: 102px;
    width: 596px;
    height: 353px;
    border: 1px solid var(--edge);
    box-sizing: border-box;
    background: var(--paper);
    overflow: hidden;
  }
  .brand {
    position: absolute;
    left: 37px;
    top: 37px;
    display: flex;
    align-items: center;
    gap: 8px;
  }
  .brand-mark {
    width: 26px;
    height: 26px;
    background: var(--teal);
  }
  .brand-name {
    color: var(--teal);
    font-weight: 600;
    font-size: 26px;
    letter-spacing: 3px;
    line-height: 1;
  }
  .identity {
    position: absolute;
    left: 0;
    right: 0;
    top: 112px;
    text-align: center;
  }
  .person-name {
    display: inline-block;
    margin: 0;
    padding: 0 12px 4px;
    font-weight: 400;
    font-size: 29px;
    color: var(--ink);
    line-height: 1.1;
    background:
      linear-gradient(to right, var(--ink) 0 50%, var(--teal) 50% 100%) bottom / 100% 2px no-repeat;
  }
  .person-role {
    margin: 6px 0 0;
    font-size: 19px;
    color: var(--ink);
  }
  .contact-band {
    position: absolute;
    left: 0;
    right: 0;
    top: 229px;
    height: 80px;
    border-top: 2px solid var(--teal);
    border-bottom: 2px solid var(--teal);
    padding: 2px 0;
    background-clip: content-box;
    background-color: var(--teal);
  }
  .contact-band p {
    margin: 0;
    color: var(--paper);
    text-align: center;
    font-size: 18.5px;
    line-height: 34px;
  }
  .contact-band p:first-child { margin-top: 3px; }
</style>
</head>
<body>
  <main class="canvas">
    <section class="card">
      <div class="brand">
        <span class="brand-mark"></span>
        <span class="brand-name">QLT</span>
      </div>
      <div class="identity">
        <h1 class="person-name">Lukas Brenning</h1>
        <p class="person-role">Certified Meridian Guide</p>
      </div>
      <div class="contact-band">
        <p class="address">3-2-48 Kamiyoshi Nakarino 164-0392 Tokyo Japan</p>
        <p class="reach">+81 70 4817 5062 &nbsp;|&nbsp; lukas.brenning@mailora.example</p>
      </div>
    </section>
  </main>
</body>
</html>
```